Update shopping site

Our current shopping website is outdated and we are wanting to update our shopping site to have a fresh new look/design.

Create a Web Design (Uncoded - PSD layout only)

We want you to develop the design for 4 pages:
1) Home Page
2) Remedy Type
3) Health Condition
4) Consultations

www.fernmoorwell.com

Reason: Close to choosing design and a few missing items to be resolved.

Industry/Entity Type

Shopping

```html
<!DOCTYPE html>
<html lang="en">
<head>
<meta charset="UTF-8">
<title>Marla Penrose, Aromatherapist</title>
<link href="https://fonts.googleapis.com/css2?family=Roboto:wght@400;500;700&display=swap" rel="stylesheet">
<style>
  :root {
    --page-bg: #f9f9f9;
    --heading: #1f4650;
    --body-text: #2f4248;
    --accent-green: #2f9e4a;
    --photo-top: #ece9e6;
    --photo-mid: #b8324a;
    --photo-bottom: #d9d4cf;
  }
  * { margin: 0; padding: 0; box-sizing: border-box; }
  html, body {
    width: 1200px;
    height: 675px;
    overflow: hidden;
    background: var(--page-bg);
    font-family: "Roboto", Arial, sans-serif;
  }
  .consultant {
    position: relative;
    width: 1200px;
    height: 675px;
  }
  .consultant-name {
    position: absolute;
    left: 232px;
    top: 120px;
    font-size: 35px;
    font-weight: 500;
    line-height: 48px;
    letter-spacing: 1.6px;
    color: var(--heading);
  }
  .consultant-label {
    position: absolute;
    left: 309px;
    top: 250px;
    font-size: 10px;
    font-weight: 700;
    letter-spacing: 1.9px;
    color: var(--heading);
  }
  .accent-rule {
    position: absolute;
    left: 283px;
    top: 309px;
    width: 26px;
    height: 3px;
    background: var(--accent-green);
  }
  .services {
    position: absolute;
    left: 309px;
    top: 353px;
    width: 312px;
    font-size: 13px;
    line-height: 22.4px;
    letter-spacing: 0.4px;
    color: var(--body-text);
  }
  .portrait {
    position: absolute;
    left: 706px;
    top: 183px;
    width: 260px;
    height: 292px;
    background: linear-gradient(180deg, var(--photo-top) 0%, var(--photo-top) 35%, var(--photo-mid) 62%, var(--photo-mid) 85%, var(--photo-bottom) 100%);
  }
</style>
</head>
<body>
  <main class="consultant">
    <h1 class="consultant-name">Marla Penrose,<br>Aromatherapist</h1>
    <p class="consultant-label">HOLISTIC READINGS</p>
    <div class="accent-rule"></div>
    <p class="services">Aura Combing, Biofield Analysis<br>$10-$75/reading. Light Therapy Treatments<br>$45/session, Crystal Light Therapy<br>$120/session, Reiki $75/session, Mind-Balance<br>$100/session.<br>Available at Fernmoor Well Herbals Wednesdays<br>or By Appointment. Call 778-555-0142 to<br>book your appointment.</p>
    <div class="portrait" role="img" aria-label="Portrait photo of the aromatherapist in a red wrap, seated on a light sofa"></div>
  </main>
</body>
</html>
```